Business Card & Logo Design

Originally the brief was for a card only - I now think it's probably better to include a logo design as well. PLease add $200 to the Budget of $210, Apologies for the inconvenience for thaos that have already submitted designs.

Lamp And Harbor Studios Pty Ltd is a video/dvd/ production company. Primarily corporate medium to high end. It's a one man operation that's been in business 20 years.

The name " Lamp and Harbor" is a primarily a reference to Lucien Marbeck film that's about film making. Shooting "Lamp and harbor" is also a technique employed by cinematographers to make scenes shot in daylight look like night.

See the design emphasising blue day/night tones but open to other ideas.

Main Text can either be Lamp and Harbor Studios or Lamp And Harbor.
Updates

Many thanks to all designers who submitted ideas for this brief.

Choosing between the designs was very difficult indeed.

I wish everyone the best and may the next job be yours!

Walter

Industry/Entity Type

Business

Requirements
Must have
• Text for card:
In Larger Print
Lamp And Harbor Studios or Lamp And Harbor
Walter Brenic
In Smaller Print
Lamp And Harbor Studios Pty Ltd.
17 Calder Lane
Marlow Park, QLD, 4817
P: 9734 2061
m: 0417 385 902
e: walterbrenic@examplemail.net

```html
<!DOCTYPE html>
<html lang="en">
<head>
<meta charset="utf-8">
<title>Lamp And Harbor Studios – Business Card</title>
<link href="https://fonts.googleapis.com/css2?family=Roboto+Condensed:wght@300;400;700&display=swap" rel="stylesheet">
<style>
  :root {
    --backdrop: #d9d9d9;
    --crimson: #94162c;
    --paper: #ffffff;
    --ink-grey: #8a8a8a;
    --soft-grey: #c9c9c9;
    --shadow: rgba(0, 0, 0, 0.28);
  }
  * { box-sizing: border-box; margin: 0; padding: 0; }
  html, body {
    width: 1200px;
    height: 900px;
    overflow: hidden;
    background: var(--backdrop);
    font-family: "Roboto Condensed", "Arial Narrow", sans-serif;
  }
  .stage {
    position: relative;
    width: 1200px;
    height: 900px;
  }

  /* Front of card */
  .card-front {
    position: absolute;
    left: 544px;
    top: 124px;
    width: 500px;
    height: 284px;
    background: var(--crimson);
    box-shadow: 2px 4px 10px var(--shadow);
  }
  .brand-dot {
    position: absolute;
    left: 205px;
    top: 88px;
    width: 64px;
    height: 64px;
    border-radius: 50%;
    background: var(--paper);
  }
  .brand-name {
    position: absolute;
    left: 0;
    right: 0;
    top: 172px;
    text-align: center;
    font-weight: 700;
    font-size: 18px;
    letter-spacing: 0.5px;
    text-transform: uppercase;
    color: var(--soft-grey);
  }

  /* Back of card */
  .card-back {
    position: absolute;
    left: 154px;
    top: 484px;
    width: 500px;
    height: 284px;
    background: var(--paper);
    border: 5px solid var(--crimson);
    box-shadow: 2px 4px 10px var(--shadow);
    overflow: hidden;
  }
  .name-band {
    position: absolute;
    left: 0;
    top: 56px;
    width: 186px;
    height: 40px;
    background: var(--crimson);
    color: var(--paper);
    font-size: 22px;
    line-height: 40px;
    padding-left: 14px;
    text-transform: uppercase;
    letter-spacing: 0.3px;
    white-space: nowrap;
  }
  .name-band .first { font-weight: 700; }
  .name-band .last { font-weight: 300; }

  .details {
    position: absolute;
    left: 36px;
    top: 116px;
    list-style: none;
    font-size: 14px;
    line-height: 20px;
    color: var(--ink-grey);
    white-space: nowrap;
  }
  .details .company {
    color: var(--crimson);
    font-size: 15px;
    margin-bottom: 1px;
  }
  .details .contact {
    display: flex;
    align-items: center;
    gap: 6px;
  }
  .details .contact svg {
    width: 11px;
    height: 11px;
    fill: var(--crimson);
    flex: none;
  }
</style>
</head>
<body>
<main class="stage">

  <section class="card-front" aria-label="Card front">
    <span class="brand-dot"></span>
    <span class="brand-name">Lamp And Harbor Studios</span>
  </section>

  <section class="card-back" aria-label="Card back">
    <h1 class="name-band"><span class="first">Walter</span> <span class="last">Brenic</span></h1>
    <ul class="details">
      <li class="company">Lamp And Harbor Studios Pty Ltd.</li>
      <li>17 Calder Lane</li>
      <li>Marlow Park, QLD, 4817</li>
      <li class="contact">
        <svg viewBox="0 0 12 12" aria-hidden="true"><path d="M1 4c0-2 2-3 5-3s5 1 5 3v1H8V4H4v1H1zM3 6h6l2 5H1z"/></svg>
        9734 2061
      </li>
      <li class="contact">
        <svg viewBox="0 0 12 12" aria-hidden="true"><path d="M3 0h6v12H3zM4 1.5v7h4v-7z"/></svg>
        0417 385 902
      </li>
      <li class="contact">
        <svg viewBox="0 0 12 12" aria-hidden="true"><path d="M0 2h12v8H0zM1.2 3.2v.4L6 6.8l4.8-3.2v-.4L6 6.2z"/></svg>
        walterbrenic@examplemail.net
      </li>
    </ul>
  </section>

</main>
</body>
</html>
```